Modern Innovative Business Card Design

We require a nice, modern, clean business card design, ready for upload to Cardwello. Our company develops online banking software solutions for small financial insitutions. The design should be clean, professional, but yet not "corporate boring". See www.fintrola.com for an idea of business image and profile. The design should communicate innovation, be modern and fresh, yet look professional and established.

Target Market(s)

Finance industry, bankers, entrepreneurs

Industry/Entity Type

Financial

Contact Information for Business Card

Daniel Hargreave
CEO

FINTROLA BV
Lindenhofstraat 38
1072 KD Amsterdam
The Netherlands

Phone: +31 20 517 8063
Direct: +31 20 446 1975
Skype: daniel.fintrola
ceo@fintrola.com
www.fintrola.com

Font styles to use
Sans Serif

Requirements
Must have
• Should look clean, modern and professional. File should be ready for upload to cardwello.
Should not have
• Boring standard corporate layout

```html
<!DOCTYPE html>
<html lang="en">
<head>
<meta charset="utf-8">
<title>Fintrola – Business Card</title>
<link rel="stylesheet" href="https://fonts.googleapis.com/css2?family=Ubuntu:wght@300;400;500&display=swap">
<style>
  :root {
    --stage: #e4e5e6;
    --card: #ffffff;
    --band: #3c3c3e;
    --green: #8cc63f;
    --green-light: #d9efbe;
    --ink: #4a4a4c;
    --ink-soft: #6b6b6d;
    --on-band: #f2f2f2;
    --on-band-soft: #c9c9cb;
    --map-dots: #e2e2e2;
  }
  * { margin: 0; padding: 0; box-sizing: border-box; }
  html, body {
    width: 1200px; height: 1000px; overflow: hidden;
    background: var(--stage);
    font-family: "Ubuntu", "Helvetica Neue", Arial, sans-serif;
  }
  .business-card {
    position: absolute; left: 180px; top: 260px;
    width: 840px; height: 480px;
    background: var(--card);
    overflow: hidden;
    box-shadow: 0 12px 30px rgba(0,0,0,.18);
  }
  .world-map {
    position: absolute; left: 250px; top: 20px;
    width: 380px; height: 180px;
    background: radial-gradient(ellipse at center, var(--map-dots) 0%, rgba(226,226,226,.5) 55%, rgba(255,255,255,0) 80%);
  }
  .website {
    position: absolute; right: 40px; top: 58px;
    color: var(--green); font-size: 19px; font-weight: 400;
  }
  .brand {
    position: absolute; left: 50px; top: 138px;
    display: flex; align-items: center; gap: 14px;
  }
  .brand-mark { width: 16px; height: 16px; background: var(--green); }
  .brand-name {
    color: var(--ink); font-size: 60px; font-weight: 400;
    letter-spacing: 2px; line-height: 1;
  }
  .contact-band {
    position: absolute; left: 0; top: 218px;
    width: 100%; height: 112px;
    background: var(--band);
  }
  .band-accent {
    position: absolute; right: 0; top: 206px;
    width: 250px; height: 12px;
    background: linear-gradient(90deg, var(--green) 0%, var(--green-light) 100%);
  }
  .band-rule {
    position: absolute; left: 0; top: 330px;
    width: 100%; height: 9px; background: var(--green);
  }
  .person { position: absolute; left: 120px; top: 240px; }
  .person-name { color: var(--green); font-size: 31px; font-weight: 500; }
  .person-title { color: var(--on-band-soft); font-size: 18px; font-weight: 300; margin-top: 8px; margin-left: 22px; }
  .direct-lines {
    position: absolute; right: 40px; top: 240px; text-align: right;
  }
  .direct-phone { color: var(--on-band); font-size: 23px; font-weight: 500; }
  .direct-email { color: var(--on-band-soft); font-size: 20px; font-weight: 300; margin-top: 8px; }
  .address {
    position: absolute; left: 120px; top: 362px;
    color: var(--ink-soft); font-size: 20px; font-weight: 300; line-height: 1.4;
    font-style: normal;
  }
  .skype {
    position: absolute; right: 40px; top: 362px;
    display: flex; align-items: center; gap: 10px;
    color: var(--ink); font-size: 20px; font-weight: 300;
  }
  .skype-dot { width: 20px; height: 20px; border-radius: 50%; background: var(--ink-soft); }
</style>
</head>
<body>
  <div class="business-card">
    <div class="world-map" role="img" aria-label="Faint dotted world map behind the logo"></div>
    <div class="website">www.fintrola.com</div>
    <div class="brand">
      <span class="brand-mark"></span>
      <span class="brand-name">FINTROLA</span>
    </div>
    <div class="band-accent"></div>
    <div class="contact-band"></div>
    <div class="band-rule"></div>
    <div class="person">
      <div class="person-name">Daniel Hargreave</div>
      <div class="person-title">CEO</div>
    </div>
    <div class="direct-lines">
      <div class="direct-phone">+31 20 446 1975</div>
      <div class="direct-email">ceo@fintrola.com</div>
    </div>
    <address class="address">
      Lindenhofstraat 38<br>
      1072 KD Amsterdam The Netherlands<br>
      +31 20 517 8063
    </address>
    <div class="skype">
      <span class="skype-dot"></span>
      <span>daniel.fintrola</span>
    </div>
  </div>
</body>
</html>
```